Kivora....... a hint of Calm

I need a web design for a new business based in London that will be mobile (offered at homes, parks or a local cafe ect) called Kivora. I offer Life Coaching/Counselling sessions, Personal training, Massage and Sports Massage. Sessions range from an hour to half and hour. My aim is to help people along their journey to help give them gain clarity of where there going, helping them to towards their goals, so that can experience bliss. My website should represent a place people can come to release their stress and worries so that they leave feeling lighter, clearer and happier. I would like my website to reflect someone feeling ALIVE. I would also like a logo design for Kivora with a sentence underneath or near saying A hint of CALM.

Target Market(s)

middle class people

Industry/Entity Type

Business

Coding

Coded - Design and coding required

Number of Pages Required

4 page

Requirements
Must have
• 1st page About us
• 2nd page Services
• 3rd page Prices
• 4th page contact details
Nice to have
• mixture of cultures in images

```html
<!DOCTYPE html>
<html lang="en">
<head>
<meta charset="utf-8">
<title>Kivora — a hint of Calm</title>
<link href="https://fonts.googleapis.com/css2?family=Raleway:wght@300;400;500;600&family=Dancing+Script:wght@700&display=swap" rel="stylesheet">
<style>
:root{
  --teal:#3dbfae;
  --teal-dark:#2aa897;
  --teal-light:#8fdcd0;
  --gold:#e3b23c;
  --gold-light:#f3cf6d;
  --ring:#f0b13a;
  --ink:#4f5557;
  --muted:#8a9193;
  --white:#ffffff;
  --line:#e6e6e6;
}
*{margin:0;padding:0;box-sizing:border-box}
html,body{width:1200px;height:3084px;overflow:hidden}
body{font-family:"Raleway",sans-serif;color:var(--ink);background:var(--white);position:relative}
.abs{position:absolute}

/* top strip + header */
.topbar{top:0;left:0;width:1200px;height:40px}
.topbar-band{position:absolute;right:0;top:0;width:760px;height:40px;background:var(--teal);border-bottom-left-radius:40px}
.topbar-info{position:absolute;top:0;height:40px;display:flex;align-items:center;gap:24px;color:var(--white);font-size:14px;right:60px}
.dot-icon{width:16px;height:16px;border-radius:50%;background:rgba(255,255,255,.85);display:inline-block}
.header{top:40px;left:0;width:1200px;height:100px;background:var(--white)}
.brand{position:absolute;left:130px;top:-32px;display:flex;align-items:center;gap:10px}
.brand-mark{width:22px;height:22px;border-radius:50%;background:var(--teal)}
.brand-name{font-size:46px;font-weight:500;color:var(--teal);letter-spacing:2px}
.nav{position:absolute;right:60px;top:40px;display:flex;gap:0}
.nav a{font-size:14px;color:var(--ink);text-decoration:none;padding:12px 22px;letter-spacing:1px}
.nav a.active{color:var(--teal);border-top:2px solid var(--teal)}

/* hero */
.hero{top:140px;left:0;width:1200px;height:560px;
  background:radial-gradient(circle at 60% 45%,#fff8d9 0,#fbe19a 18%,#f5c052 40%,#e59a2c 72%,#b8741f 100%)}
.hero-text{position:absolute;left:110px;top:260px;color:var(--white)}
.hero-text .script{font-family:"Dancing Script",cursive;font-size:60px;color:#5b3a1a;line-height:1}
.hero-text .big{font-family:"Raleway",sans-serif;font-size:92px;font-weight:300;letter-spacing:6px;color:var(--teal);line-height:1}
.dots{position:absolute;bottom:14px;left:0;width:100%;display:flex;justify-content:center;gap:12px}
.dots span{width:10px;height:10px;border-radius:50%;background:rgba(255,255,255,.6)}
.dots span.on{background:var(--white)}

/* offer heading */
.offer-head{top:780px;left:0;width:1200px;text-align:center}
.offer-head h2{font-family:"Dancing Script",cursive;font-size:56px;color:var(--gold);font-weight:700}
.offer-head svg{margin-top:6px}

/* services */
.service{left:0;width:1200px;height:360px}
.service.teal{background:linear-gradient(180deg,#53c9b8 0%,var(--teal) 50%,#6fd2c3 100%)}
.service h3{position:absolute;font-size:40px;font-weight:400;color:var(--ink)}
.service.teal h3{color:var(--white)}
.service .rule{position:absolute;width:500px;height:14px}
.service p{position:absolute;font-size:13px;line-height:22px;color:var(--muted)}
.service.teal p{color:#eafaf7}
.photo-circle{position:absolute;width:210px;height:210px;border-radius:50%;border:8px solid var(--ring);box-shadow:0 0 0 6px var(--white)}

/* contact strip */
.contact{top:2480px;left:0;width:1200px;height:208px;background:var(--white)}
.contact .col{position:absolute;top:56px}
.contact .label{font-size:14px;color:var(--ink);margin-bottom:14px}
.contact .value{font-size:22px;color:var(--ink);display:flex;align-items:center;gap:10px}
.contact .small{font-size:11px;color:var(--muted);margin-top:6px}
.subscribe{display:flex;align-items:center;width:360px;height:36px;border:1px solid var(--line);border-radius:18px;padding:0 16px;font-size:12px;color:#aaa;justify-content:space-between}

/* footer */
.footer{top:2688px;left:0;width:1200px;height:396px;background:linear-gradient(180deg,var(--gold) 0%,#dca930 100%);color:var(--white)}
.f-brand{position:absolute;left:96px;top:56px;display:flex;align-items:center;gap:10px}
.f-brand .brand-mark{background:var(--white)}
.f-brand .brand-name{color:var(--white);font-size:40px}
.f-copy{position:absolute;left:96px;top:160px;font-size:12px;line-height:20px}
.f-col{position:absolute;top:56px}
.f-col h4{font-family:"Dancing Script",cursive;font-size:30px;font-weight:700;margin-bottom:14px}
.f-col ul{list-style:none;font-size:13px;line-height:34px}
.f-col ul li{border-bottom:1px solid rgba(255,255,255,.35);width:170px}
.socials{display:flex;gap:16px;margin-bottom:30px}
.socials span{width:22px;height:22px;border-radius:50%;background:var(--white)}
.timing{font-size:13px;line-height:26px}
.timing td{padding-right:22px}
</style>
</head>
<body>

<div class="abs topbar">
  <div class="topbar-band"></div>
  <div class="topbar-info">
    <span class="dot-icon"></span><span class="dot-icon"></span><span class="dot-icon"></span>
    <span>support@kivora.co.uk</span>
    <span>(020) 400-0123</span>
  </div>
</div>

<header class="abs header">
  <div class="brand"><span class="brand-mark"></span><span class="brand-name">Kivora</span></div>
  <nav class="nav">
    <a class="active" href="#">HOME</a><a href="#">ABOUT US</a><a href="#">SERVICES</a><a href="#">PRICES</a><a href="#">CONTACT</a>
  </nav>
</header>

<section class="abs hero" role="img" aria-label="Woman with arms raised against a golden sunset over the sea">
  <div class="hero-text">
    <div class="script">A hint of</div>
    <div class="big">CALM</div>
  </div>
  <div class="dots"><span class="on"></span><span></span><span></span><span></span></div>
</section>

<div class="abs offer-head">
  <h2>What We Offer</h2>
  <svg width="160" height="14" viewBox="0 0 160 14"><line x1="0" y1="7" x2="68" y2="7" stroke="#e3b23c" stroke-width="1.5"/><circle cx="80" cy="7" r="4" fill="#e3b23c"/><line x1="92" y1="7" x2="160" y2="7" stroke="#e3b23c" stroke-width="1.5"/></svg>
</div>

<section class="abs service" style="top:920px">
  <div class="photo-circle" role="img" aria-label="Coach in conversation with a client" style="left:130px;top:40px;background:radial-gradient(circle,#f4d9c2,#c9a07f)"></div>
  <h3 style="left:420px;top:50px">Life/personal Performance Coaching</h3>
  <svg class="rule" style="left:420px;top:110px" viewBox="0 0 500 14"><line x1="0" y1="7" x2="500" y2="7" stroke="#e3b23c"/><circle cx="250" cy="7" r="3" fill="#e3b23c"/></svg>
  <p style="left:420px;top:140px;width:690px">I offer sessions that empower people to discover their true values, desires and ambitions, and help them achieve their goals in life. I offer a calm, non-judgemental and supportive environment that blends goal setting and action planning to enable this process. I hold you accountable for actions you set and support you on your journey in a warm and friendly way. I address confidence and relationship issues, business, parenting, spirituality, finances, career and more.</p>
</section>

<section class="abs service teal" style="top:1320px">
  <h3 style="left:80px;top:90px">Angel Readings</h3>
  <svg class="rule" style="left:80px;top:150px" viewBox="0 0 500 14"><line x1="0" y1="7" x2="500" y2="7" stroke="#ffffff"/><circle cx="250" cy="7" r="3" fill="#ffffff"/></svg>
  <p style="left:80px;top:180px;width:700px">An angel reading provides you with guidance and direction for your life. It can also give you insight into your future, based on the path that you are following at present. Readings are performed intuitively through the guidance received.</p>
  <div class="photo-circle" role="img" aria-label="Smiling woman in warm natural light" style="left:880px;top:70px;background:radial-gradient(circle,#fde6b5,#e7a24a)"></div>
</section>

<section class="abs service" style="top:1720px">
  <div class="photo-circle" role="img" aria-label="Two people stretching during a training session" style="left:130px;top:50px;background:radial-gradient(circle,#f1efe9,#c7c0b2)"></div>
  <h3 style="left:420px;top:80px">Personal training</h3>
  <svg class="rule" style="left:420px;top:140px" viewBox="0 0 500 14"><line x1="0" y1="7" x2="500" y2="7" stroke="#e3b23c"/><circle cx="250" cy="7" r="3" fill="#e3b23c"/></svg>
  <p style="left:420px;top:170px;width:690px">Personal training offers one on one sessions as a fitness professional who prescribes exercise and nutritional plans to help you achieve your personal goals. The trainer also provides feedback and holds clients accountable. Private training is paced to match and measure your progress, the work and the effort that fits with you.</p>
</section>

<section class="abs service teal" style="top:2120px">
  <h3 style="left:80px;top:130px">Sports Massage &amp; Massage</h3>
  <svg class="rule" style="left:80px;top:190px" viewBox="0 0 500 14"><line x1="0" y1="7" x2="500" y2="7" stroke="#ffffff"/><circle cx="250" cy="7" r="3" fill="#ffffff"/></svg>
  <p style="left:80px;top:220px;width:700px">Sports massage and massage is a great way to relieve tension, relax the body, release aches and return into the body, improve circulation, and reduce pain. It offers an excellent opportunity to take time out for yourself, ensure that your body is looked after well, and that you experience bliss.</p>
  <div class="photo-circle" role="img" aria-label="Person relaxing during a massage" style="left:880px;top:70px;background:radial-gradient(circle,#f0d7b8,#9b6a3e)"></div>
</section>

<section class="abs contact">
  <div class="col" style="left:80px">
    <div class="label">Book by Phone</div>
    <div class="value"><svg width="18" height="18" viewBox="0 0 24 24"><path d="M6.6 10.8a15 15 0 0 0 6.6 6.6l2.2-2.2a1 1 0 0 1 1-.25 11.4 11.4 0 0 0 3.6.57 1 1 0 0 1 1 1V20a1 1 0 0 1-1 1A17 17 0 0 1 3 4a1 1 0 0 1 1-1h3.5a1 1 0 0 1 1 1c0 1.25.2 2.45.57 3.6a1 1 0 0 1-.25 1z" fill="#3dbfae"/></svg>0 700 400 1234</div>
    <div class="small">Booking from 8am – 7pm</div>
  </div>
  <div class="col" style="left:420px">
    <div class="label">Services and Support</div>
    <div class="value" style="font-size:20px">hello.kivora@mailbox.co.uk</div>
    <div class="small">Get your doubts cleared</div>
  </div>
  <div class="col" style="left:760px">
    <div class="label">Subscribe for the latest deals</div>
    <div class="subscribe"><span>Enter your Email Address</span><svg width="16" height="16" viewBox="0 0 24 24"><path d="M2 21l21-9L2 3v7l15 2-15 2z" fill="#e3b23c"/></svg></div>
    <div class="small">Subscribe to our email newsletter</div>
  </div>
</section>

<footer class="abs footer">
  <div class="f-brand"><span class="brand-mark"></span><span class="brand-name">Kivora</span></div>
  <div class="f-copy">© 2024<br>All Rights Reserved</div>

  <div class="f-col" style="left:380px">
    <h4>Follow us</h4>
    <div class="socials"><span></span><span></span><span></span></div>
    <h4>Timing</h4>
    <table class="timing">
      <tr><td>Mon - Fri</td><td>8:00am – 7:00pm</td></tr>
      <tr><td>Sat</td><td>9:00am – 5:00pm</td></tr>
      <tr><td>Sun</td><td>Closed</td></tr>
    </table>
  </div>

  <div class="f-col" style="left:700px">
    <h4>Navigation</h4>
    <ul><li>Home</li><li>About Us</li><li>Services</li><li>Prices</li><li>Contact Us</li></ul>
  </div>

  <div class="f-col" style="left:950px">
    <h4>Services</h4>
    <ul><li>Life/Personal Performance</li><li>Coaching</li><li>Angel Readings</li><li>Personal training</li><li>Sports Massage &amp; Massage</li></ul>
  </div>
</footer>

</body>
</html>
```